Business card for STEADYWAVE

Please design professional business card for IT consulting firm STEADYWAVE INC.
Use logo attached.
Use information from sample qNode business card attached.
replace qnode inc with STEADYWAVE INC.
as well as qnodeinc.com with steadywave.example

```html
<!DOCTYPE html>
<html lang="en">
<head>
<meta charset="utf-8">
<title>STEADYWAVE – Business Card</title>
<link rel="stylesheet" href="https://fonts.googleapis.com/css2?family=Open+Sans:wght@400;600;700&display=swap">
<style>
  :root {
    --bg: #d6d6d6;
    --purple: #661190;
    --purple-name: #6a1591;
    --ink: #111111;
    --paper: #ffffff;
  }
  * { box-sizing: border-box; margin: 0; padding: 0; }
  html, body { width: 1200px; height: 1200px; overflow: hidden; }
  body {
    background: var(--bg);
    font-family: "Open Sans", Arial, sans-serif;
    color: var(--ink);
    position: relative;
  }
  .card {
    position: absolute;
    left: 250px;
    width: 700px;
    height: 400px;
  }
  .card-front {
    top: 150px;
    background: var(--purple);
    display: flex;
    align-items: center;
    justify-content: center;
  }
  .front-wordmark {
    color: var(--paper);
    font-weight: 600;
    font-size: 50px;
    letter-spacing: 6px;
  }
  .card-back {
    top: 650px;
    background: var(--paper);
    padding: 58px 62px 0 62px;
  }
  .back-wordmark {
    display: flex;
    align-items: center;
    gap: 14px;
    font-weight: 700;
    font-size: 48px;
    letter-spacing: 5px;
    line-height: 1;
  }
  .wordmark-square {
    width: 18px;
    height: 18px;
    background: var(--purple);
  }
  .person-name {
    margin-top: 10px;
    color: var(--purple-name);
    font-weight: 700;
    font-size: 31px;
    letter-spacing: -0.3px;
    line-height: 1.1;
    white-space: nowrap;
  }
  .person-title {
    font-size: 19px;
    line-height: 1.2;
  }
  .contact-row {
    margin-top: 14px;
    display: flex;
    align-items: stretch;
    font-size: 18px;
    line-height: 1.3;
    white-space: nowrap;
  }
  .contact-col { padding-right: 16px; }
  .contact-col + .contact-col {
    border-left: 2px solid var(--ink);
    padding-left: 16px;
    padding-right: 0;
  }
  .company-block {
    margin-top: 16px;
    border-top: 3px solid var(--ink);
    border-bottom: 3px solid var(--ink);
    padding: 8px 0 10px;
    font-size: 18px;
    line-height: 1.3;
    white-space: nowrap;
  }
  .company-name { font-weight: 700; font-size: 20px; }
</style>
</head>
<body>
  <section class="card card-front">
    <div class="front-wordmark">STEADYWAVE</div>
  </section>

  <section class="card card-back">
    <div class="back-wordmark">
      <span>STEADYWAVE</span>
      <span class="wordmark-square"></span>
    </div>
    <div class="person-name">DORIAN VELASKO, P. ENG.</div>
    <div class="person-title">GENERAL MANAGER</div>
    <div class="contact-row">
      <div class="contact-col">
        <div>(555) 286-0170 est.201</div>
        <div>dvelasko@steadywave.example</div>
      </div>
      <div class="contact-col">
        <div>(555) 897-0142</div>
        <div>www.steadywave.example</div>
      </div>
    </div>
    <div class="company-block">
      <div><span class="company-name">STEADYWAVE INC.</span> 1280 Harbourline Rd., Suite 101</div>
      <div>Brookfield, Ontario, A1B 2C3, Canada</div>
    </div>
  </section>
</body>
</html>
```